Flyer for Car Detailing Shop

I am opening a detailing shop. I am looking for a nice, easy to read single sided flyer I can hand out at car shows, hang in store windows and to my clients and customers to promote my business. I want it a little professional yet attention grabbing. I want someone to look at it and go "holy shit, thats a nice flyer" haha

Here are some things that must be included:
- Company Name: Brightfern Motorworks Detailing & Coatings
- Tag Line: The Science of Detailing
- Address: 4150 Harlow Rd, Brindlewood, ST 00190
- www.brightfernmotor.example
- Find Us on social Media! ::insert facebook and instagram logo
Colors: Black, Lime Green and Purple for accents, etc

HAND WASH
- Express Wash start at $25
- Deluxe Wash Start at $50

EXTERIOR DETAILING
-Basic Packages Start at $160
- Deluxe Packages Start at $350

INTERIOR DETAILING
- Basic Packages Start at $60
- Deluxe Packages Start at $200

New Car Prep and Ceramic Coatings
*Consultation required prior to beginning work*
- Paint: Starting at $500
- Interior: Starting at $100
- Wheels Off: Starting at $200
- Trim: Starting at $100
- Windows: $50 windshield/ $25 per pane

Additional Services
- Scratch removal
- Ozone Treatment
- Headlight Restoration
- Chip Repair

```html
<!DOCTYPE html>
<html lang="en">
<head>
<meta charset="utf-8">
<title>Brightfern Motorworks Detailing &amp; Coatings</title>
<link rel="stylesheet" href="https://fonts.googleapis.com/css2?family=Lato:ital,wght@0,400;0,700;1,700&family=Montserrat:wght@300;800;900&display=swap">
<style>
  :root {
    --page-bg: #4a4a4a;
    --forest: #3d8a43;
    --forest-deep: #2a6a31;
    --lime: #52b848;
    --ink: #0b0b0b;
    --paper: #ffffff;
    --car-red: #c4161c;
    --car-dark: #6a0a0e;
  }
  * { box-sizing: border-box; margin: 0; padding: 0; }
  html, body { width: 1200px; height: 1200px; overflow: hidden; }
  body { background: var(--page-bg); position: relative; font-family: "Lato", sans-serif; color: var(--ink); }

  .flyer { position: absolute; left: 150px; top: 21px; width: 900px; height: 1158px; background: var(--paper); overflow: hidden; }

  .hero-bg { position: absolute; left: 0; top: 0; width: 900px; height: 700px; }
  .hero-photo { position: absolute; left: 0; top: 0; width: 900px; height: 600px;
    background: linear-gradient(135deg, #4f9a55 0%, var(--forest) 45%, var(--forest-deep) 100%); }
  .waves { position: absolute; left: 0; top: 0; width: 900px; height: 700px; }

  .brand-mark { position: absolute; left: 30px; top: 130px; width: 200px; text-align: center; color: var(--paper); }
  .brand-mark .dot { width: 64px; height: 64px; border-radius: 50%; border: 3px solid var(--paper); margin: 0 auto 14px; }
  .brand-mark .name { font-family: "Lato", sans-serif; font-weight: 700; font-size: 25px; line-height: 1.1; }

  .headline { position: absolute; left: 395px; top: 58px; width: 480px; text-align: center; color: var(--paper);
    font-family: "Lato", sans-serif; font-style: italic; font-weight: 700; font-size: 41px; line-height: 51px; }
  .tagline { position: absolute; left: 400px; top: 176px; width: 450px; display: flex; align-items: center; gap: 12px;
    color: var(--paper); font-family: "Montserrat", sans-serif; font-weight: 300; font-size: 23px; letter-spacing: 0.5px; white-space: nowrap; }
  .tagline::before, .tagline::after { content: ""; flex: 1; height: 1.5px; background: var(--paper); }

  .car-photo { position: absolute; left: 18px; top: 320px; width: 700px; height: 350px; border-radius: 48% 46% 30% 30% / 55% 55% 25% 25%;
    background: radial-gradient(ellipse at 55% 40%, #e23a3f 0%, var(--car-red) 45%, var(--car-dark) 100%); }

  .wash-badge { position: absolute; left: 611px; top: 248px; width: 194px; height: 194px; border-radius: 50%;
    background: var(--ink); border: 12px solid var(--lime); display: flex; align-items: center; justify-content: center; }
  .wash-badge span { font-family: "Montserrat", sans-serif; font-weight: 900; font-size: 43px; line-height: 40px; color: var(--paper);
    text-align: center; transform: rotate(-8deg); display: block; }

  .services { position: absolute; left: 0; top: 690px; width: 900px; height: 125px; }
  .svc { position: absolute; top: 0; }
  .svc h2, .coatings h2, .extras h2 { font-family: "Montserrat", sans-serif; font-weight: 800; font-size: 25px; line-height: 26px; color: var(--ink); }
  .svc p, .coatings li, .extras li { font-size: 16px; line-height: 26px; }
  .svc ul { list-style: none; margin-top: 12px; }
  .svc b, .coatings b { font-weight: 700; }
  .svc-hand { left: 37px; }
  .svc-ext { left: 261px; }
  .svc-ext ul { padding-left: 33px; }
  .svc-int { left: 588px; }
  .svc-int ul { padding-left: 31px; }
  .rule { position: absolute; width: 2px; background: var(--lime); }

  .coatings { position: absolute; left: 39px; top: 837px; width: 390px; }
  .coatings ul, .extras ul { list-style: none; }
  .coatings ul { margin-top: 8px; }
  .coatings li, .extras li { position: relative; padding-left: 26px; }
  .coatings li::before, .extras li::before { content: ""; position: absolute; left: 5px; top: 9px; width: 8px; height: 8px; border-radius: 50%; background: var(--ink); }

  .extras { position: absolute; left: 516px; top: 850px; width: 360px; }
  .extras ul { margin-top: 12px; display: grid; grid-template-columns: 192px 1fr; column-gap: 0; }
  .extras li { padding-left: 22px; }
  .extras li::before { left: 3px; }

  .thumb { position: absolute; top: 943px; width: 104px; height: 104px; border-radius: 50%; border: 6px solid var(--lime); }
  .thumb-engine { left: 508px; background: radial-gradient(circle, #9a9ea3, #3a3d42); }
  .thumb-light { left: 628px; background: radial-gradient(circle, #d2384a, #2b2a5a); }
  .thumb-lift { left: 749px; background: radial-gradient(circle, #c7ccd3, #4b5563); }

  .footer { position: absolute; left: 0; top: 1068px; width: 900px; height: 90px; background: var(--ink); }
  .footer-band { position: absolute; left: 0; top: 0; width: 484px; height: 90px; background: var(--lime);
    clip-path: polygon(0 0, 100% 0, 94.5% 100%, 0 100%); }
  .contact { position: absolute; left: 42px; top: 16px; font-size: 16px; line-height: 26px; color: var(--ink); }
  .contact div { display: flex; align-items: center; gap: 9px; }
  .contact svg { width: 17px; height: 17px; }
  .social { position: absolute; left: 535px; top: 23px; display: flex; align-items: center; gap: 6px; color: var(--paper); font-size: 16px; }
  .social .label { margin-right: 16px; }
  .social .chip { width: 24px; height: 24px; border-radius: 50%; border: 2px solid var(--paper); }
</style>
</head>
<body>
<main class="flyer">
  <div class="hero-bg">
    <div class="hero-photo" role="img" aria-label="Green-toned photo of cars inside a detailing garage"></div>
    <svg class="waves" viewBox="0 0 900 700" aria-hidden="true">
      <path d="M0,293 C250,240 500,500 700,500 C800,500 860,480 900,449 V700 H0 Z" fill="var(--lime)"/>
      <path d="M0,372 C250,310 500,580 700,560 C800,550 860,530 900,520 V700 H0 Z" fill="var(--ink)"/>
      <path d="M0,440 C250,380 500,640 700,630 C800,622 860,600 900,570 V700 H0 Z" fill="var(--paper)"/>
    </svg>
  </div>

  <div class="brand-mark">
    <div class="dot"></div>
    <div class="name">Brightfern Motorworks</div>
  </div>

  <h1 class="headline">Brightfern Motorworks<br>Detailing &amp; Coatings</h1>
  <p class="tagline">The Science of Detailing</p>

  <div class="car-photo" role="img" aria-label="Photo of a glossy red hatchback car"></div>

  <div class="wash-badge"><span>CAR<br>WASH</span></div>

  <section class="services">
    <div class="svc svc-hand">
      <h2>HAND WASH</h2>
      <ul>
        <li><p>Express Wash start at <b>$25</b></p></li>
        <li><p>Deluxe Wash Start at <b>$50</b></p></li>
      </ul>
    </div>
    <div class="rule" style="left:245px; top:-6px; height:130px;"></div>
    <div class="svc svc-ext">
      <h2>EXTERIOR DETAILING</h2>
      <ul>
        <li><p>Basic Packages Start at <b>$160</b></p></li>
        <li><p>Deluxe Packages Start at <b>$350</b></p></li>
      </ul>
    </div>
    <div class="rule" style="left:570px; top:-6px; height:130px;"></div>
    <div class="svc svc-int">
      <h2>INTERIOR DETAILING</h2>
      <ul>
        <li><p>Basic Packages Start at <b>$60</b></p></li>
        <li><p>Deluxe Packages Start at <b>$200</b></p></li>
      </ul>
    </div>
  </section>

  <section class="coatings">
    <h2>NEW CAR PREP AND<br>CERAMIC COATINGS</h2>
    <ul>
      <li>Consultation required prior to beginning work*</li>
      <li>Paint: Starting at <b>$500</b></li>
      <li>Interior: Starting at <b>$100</b></li>
      <li>Wheels Off: Starting at <b>$200</b></li>
      <li>Trim: Starting at <b>$100</b></li>
      <li>Windows : <b>$50</b> windshield/ <b>$25</b> per pane</li>
    </ul>
  </section>

  <div class="rule" style="left:440px; top:837px; height:205px;"></div>

  <section class="extras">
    <h2>ADDITIONAL SERVICES</h2>
    <ul>
      <li>Scratch removal</li>
      <li>Ozone Treatment</li>
      <li>Headlight Restoration</li>
      <li>Chip Repair</li>
    </ul>
  </section>

  <div class="thumb thumb-engine" role="img" aria-label="Photo of hands working in an engine bay"></div>
  <div class="thumb thumb-light" role="img" aria-label="Photo of a car tail light close-up"></div>
  <div class="thumb thumb-lift" role="img" aria-label="Photo of a car raised on a service lift"></div>

  <footer class="footer">
    <div class="footer-band"></div>
    <div class="contact">
      <div>
        <svg viewBox="0 0 24 24" aria-hidden="true"><path d="M12 2a7 7 0 0 0-7 7c0 5 7 13 7 13s7-8 7-13a7 7 0 0 0-7-7zm0 9.5A2.5 2.5 0 1 1 12 6.5a2.5 2.5 0 0 1 0 5z" fill="var(--ink)"/></svg>
        <span>4150 Harlow Rd, Brindlewood, ST 00190</span>
      </div>
      <div>
        <svg viewBox="0 0 24 24" aria-hidden="true"><circle cx="12" cy="12" r="9" fill="none" stroke="var(--ink)" stroke-width="2.4"/><path d="M3 12h18M12 3c3 3 3 15 0 18M12 3c-3 3-3 15 0 18" fill="none" stroke="var(--ink)" stroke-width="1.6"/></svg>
        <span>www.brightfernmotor.example</span>
      </div>
    </div>
    <div class="social">
      <span class="label">Find Us on social Media !</span>
      <span class="chip"></span>
      <span class="chip"></span>
    </div>
  </footer>
</main>
</body>
</html>
```